Business card for Northland's Blue Wagon.

Good day i am looking for a business card design for my business.
The name of the business is Northland's Blue Wagon. It is a van rental business that provides a driver and helper to the customer. Customer have use to van for small moves, studio or 1 bedroom, Moving furniture like couch or kitchen cabinets.
We are available evenings, weekends and holidays.
the means to contact us is by phone at 628-947-2071; By emails at Oakridge@northlandsbluewagon.net; or by social media, Facebook and Instagram.
You can see attached pictures of the van and or logo.

```html
<!DOCTYPE html>
<html lang="en">
<head>
<meta charset="utf-8">
<title>Northland's Blue Wagon – Business Card</title>
<link rel="stylesheet" href="https://fonts.googleapis.com/css2?family=Roboto:wght@400;500;700&display=swap">
<style>
  :root {
    --stage: #232323;
    --paper: #ffffff;
    --brand-red: #e11f26;
    --ink: #111111;
    --ink-soft: #222222;
  }
  * { margin: 0; padding: 0; box-sizing: border-box; }
  html, body {
    width: 1200px; height: 711px; overflow: hidden;
    background: var(--stage);
    font-family: "Roboto", Arial, sans-serif;
  }
  .stage { position: relative; width: 1200px; height: 711px; }

  .card {
    position: absolute;
    width: 540px; height: 309px;
    background: var(--paper);
    overflow: hidden;
  }
  .card--front { left: 40px; top: 201px; }
  .card--back  { left: 620px; top: 201px; }

  /* brand name standing in place of the mark */
  .brand {
    position: absolute;
    display: flex; align-items: center; gap: 10px;
    color: var(--brand-red);
    font-weight: 700;
    line-height: 1.1;
  }
  .brand__dot {
    flex: none;
    border-radius: 50%;
    background: var(--brand-red);
  }
  .card--front .brand {
    left: 0; right: 0; top: 0; bottom: 0;
    justify-content: center;
    font-size: 26px;
  }
  .card--front .brand__dot { width: 26px; height: 26px; }

  .card--back .brand {
    left: 34px; top: 62px; width: 220px;
    font-size: 21px;
  }
  .card--back .brand__dot { width: 22px; height: 22px; }

  /* name block */
  .accent-bar {
    position: absolute; right: 0; top: 118px;
    width: 18px; height: 58px;
    background: var(--brand-red);
  }
  .person {
    position: absolute; right: 30px; top: 120px;
    text-align: right;
  }
  .person__name {
    font-size: 30px; font-weight: 700; letter-spacing: 0.2px;
    color: var(--ink); line-height: 1;
  }
  .person__first { color: var(--brand-red); }
  .person__role {
    margin-top: 4px;
    font-size: 13px; font-weight: 400; color: var(--ink-soft);
  }
  .divider {
    position: absolute; left: 28px; right: 18px; top: 186px;
    height: 1px; background: var(--brand-red);
  }

  /* contacts */
  .contacts {
    position: absolute; left: 30px; top: 200px;
    list-style: none;
  }
  .contacts__item {
    display: flex; align-items: center; gap: 8px;
    height: 22px;
    font-size: 15px; font-weight: 500; color: var(--ink);
  }
  .contacts__icon { width: 14px; height: 14px; flex: none; }
  .contacts__social { display: flex; gap: 4px; }
  .contacts__social span {
    width: 14px; height: 14px; border-radius: 50%;
    background: var(--brand-red);
  }
</style>
</head>
<body>
<main class="stage">

  <section class="card card--front" aria-label="Card front">
    <div class="brand"><span class="brand__dot"></span>Northland's Blue Wagon</div>
  </section>

  <section class="card card--back" aria-label="Card back">
    <div class="brand"><span class="brand__dot"></span>Northland's Blue Wagon</div>

    <div class="accent-bar"></div>
    <div class="person">
      <p class="person__name"><span class="person__first">Marta</span> Kolarova</p>
      <p class="person__role">Co-Founder</p>
    </div>
    <div class="divider"></div>

    <ul class="contacts">
      <li class="contacts__item">
        <svg class="contacts__icon" viewBox="0 0 24 24" aria-hidden="true">
          <path fill="#e11f26" d="M6.6 10.8a15.1 15.1 0 0 0 6.6 6.6l2.2-2.2c.3-.3.7-.4 1-.2 1.1.4 2.3.6 3.6.6.6 0 1 .4 1 1V20c0 .6-.4 1-1 1A17 17 0 0 1 3 4c0-.6.4-1 1-1h3.5c.6 0 1 .4 1 1 0 1.3.2 2.5.6 3.6.1.3 0 .7-.2 1z"/>
        </svg>
        628-947-2071
      </li>
      <li class="contacts__item">
        <span class="contacts__social" aria-hidden="true"><span></span><span></span></span>
        @northlandsbluewagon
      </li>
      <li class="contacts__item">
        <svg class="contacts__icon" viewBox="0 0 24 24" aria-hidden="true">
          <circle cx="12" cy="12" r="10" fill="none" stroke="#e11f26" stroke-width="2"/>
          <path d="M2 12h20M12 2c3 3 3 17 0 20M12 2c-3 3-3 17 0 20" fill="none" stroke="#e11f26" stroke-width="1.6"/>
        </svg>
        www.northlandsbluewagon.net
      </li>
      <li class="contacts__item">
        <svg class="contacts__icon" viewBox="0 0 24 24" aria-hidden="true">
          <rect x="2" y="5" width="20" height="14" rx="1.5" fill="#e11f26"/>
          <path d="M3 6l9 7 9-7" fill="none" stroke="#fff" stroke-width="1.8"/>
        </svg>
        Oakridge@northlandsbluewagon.net
      </li>
    </ul>
  </section>

</main>
</body>
</html>
```